Stationery Design Project

KT7 Staffing requires letterhead and business card designs for a company based in London. Just like the name, we're a management resourcing company, providing resources to third party companies. You can see www.kt7staffing-example.com for ideas on existing colour schemes and design concepts that have been implimented and agreed to. Ultimately the design should broadcast professionalism, safety and the concept of growth.

Target Market(s)

Financial institutes; friendly societies (All UK based)

Industry/Entity Type

Safety

Requirements
Must have
• Files produced should be print ready; and the text in them editable (eg address, name etc)

```html
<!DOCTYPE html>
<html lang="en">
<head>
<meta charset="utf-8">
<title>KT7 Staffing – Letterhead</title>
<link href="https://fonts.googleapis.com/css2?family=Arimo:wght@400;700&display=swap" rel="stylesheet">
<style>
  :root {
    --paper: #f5f9fb;
    --brand-teal: #1f8a95;
    --brand-sky: #6ab4cf;
    --contact-teal: #1c7e89;
    --decor-tint: #e3eef3;
  }
  html, body {
    margin: 0;
    padding: 0;
    overflow: hidden;
  }
  body {
    width: 930px;
    height: 1200px;
    background: var(--paper);
    font-family: "Arimo", Arial, sans-serif;
  }
  .letterhead {
    position: relative;
    width: 930px;
    height: 1200px;
    overflow: hidden;
    background: var(--paper);
  }
  .background-decor {
    position: absolute;
    left: 290px;
    top: 410px;
    width: 640px;
    height: 790px;
    background: radial-gradient(ellipse at 70% 55%, var(--decor-tint) 0%, rgba(227, 238, 243, 0.6) 45%, rgba(245, 249, 251, 0) 75%);
  }
  .brand {
    position: absolute;
    left: 60px;
    top: 62px;
    display: flex;
    align-items: center;
    gap: 22px;
  }
  .brand-mark {
    width: 78px;
    height: 78px;
    background: var(--brand-sky);
  }
  .brand-name {
    margin: 0;
    font-size: 64px;
    font-weight: 700;
    letter-spacing: -1px;
    color: var(--brand-teal);
    line-height: 1;
  }
  .contact {
    position: absolute;
    left: 170px;
    top: 208px;
    margin: 0;
    font-style: normal;
    font-size: 17px;
    line-height: 23px;
  }
  .contact-line {
    display: block;
  }
  .contact-address {
    color: var(--brand-sky);
  }
  .contact-direct {
    color: var(--contact-teal);
  }
</style>
</head>
<body>
  <main class="letterhead">
    <div class="background-decor" role="img" aria-label="Faint large brand decoration in soft pale blue"></div>

    <header class="brand">
      <div class="brand-mark" aria-hidden="true"></div>
      <h1 class="brand-name">KT7 Staffing</h1>
    </header>

    <address class="contact">
      <span class="contact-line contact-address">Harbour Yard,</span>
      <span class="contact-line contact-address">Calder Row, London</span>
      <span class="contact-line contact-direct">0123 555 014</span>
      <span class="contact-line contact-direct">ellis@kt7staffing-example.com</span>
      <span class="contact-line contact-direct">www.kt7staffing-example.com</span>
    </address>
  </main>
</body>
</html>
```